Marrowby Lane School bookmark

We need a vertical card (DL 99x210 mm) that will be put inside books at a primary school for children to make comments about the books. Text at the top:
Marrowby Lane School (and logo)
What did you think of this book?

Text at the bottom:
Pass it on!

Words in repeated pattern around the edge: funny sad exciting mysterious fantastic boring enthralling interesting

It should be in interesting bright colours with a white or pale background as children will write on the cards

The card should be double sided with the same design on each side

Industry/Entity Type

School

```html
<!DOCTYPE html>
<html lang="en">
<head>
<meta charset="utf-8">
<title>Marrowby Lane School Bookmark</title>
<link href="https://fonts.googleapis.com/css2?family=Open+Sans:wght@600&family=Shadows+Into+Light&family=Special+Elite&display=swap" rel="stylesheet">
<style>
  :root {
    --red: #c8202f;
    --black: #111111;
    --white: #ffffff;
    --panel-top: #c9c9c9;
    --panel-bottom: #ffffff;
    --title-pink: #d9646c;
    --ink: #333333;
    --orange: #f7941d;
    --yellow: #ffc20e;
    --green: #8dc63f;
    --teal: #17b1a8;
    --blue: #1c75bc;
    --navy: #1b1a8c;
    --purple: #662d91;
    --magenta: #d4145a;
    --art-warm: #e9c9a4;
    --art-cool: #b9cde6;
  }
  * { margin: 0; padding: 0; box-sizing: border-box; }
  html, body { width: 1200px; height: 2544px; overflow: hidden; background: var(--white); }
  .bookmark { position: relative; width: 1200px; height: 2544px; background: var(--white); overflow: hidden; }
  .frame-art { position: absolute; inset: 0; }
  .school-name {
    position: absolute; left: 326px; right: 30px; top: 62px;
    text-align: right; white-space: nowrap;
    font-family: "Open Sans", sans-serif; font-weight: 600;
    font-size: 58px; letter-spacing: 2px; color: var(--red); line-height: 1;
  }
  .school-badge {
    position: absolute; left: 48px; top: 70px; width: 246px; height: 246px;
    border-radius: 50%; background: var(--red); border: 8px solid var(--black);
    display: flex; align-items: center; justify-content: center; text-align: center;
    font-family: "Open Sans", sans-serif; font-weight: 600; font-size: 30px;
    line-height: 1.15; color: var(--white); padding: 30px;
  }
  .reader-art {
    position: absolute; left: 117px; top: 297px; width: 355px; height: 276px;
    border-radius: 30px; background: linear-gradient(160deg, var(--art-warm), #c9473f);
  }
  .prompt {
    position: absolute; left: 488px; top: 328px; width: 604px; text-align: center;
    white-space: nowrap;
    font-family: "Special Elite", monospace; font-size: 48px; line-height: 1.45;
    color: var(--title-pink); font-weight: 400;
  }
  .word-tab {
    position: absolute; width: 95px; height: 252px;
    display: flex; align-items: center; justify-content: center;
  }
  .word-tab span {
    font-family: "Shadows Into Light", cursive; font-size: 46px; color: var(--white);
    white-space: nowrap; display: block;
  }
  .side-left .word-tab { left: 0; }
  .side-left .word-tab span { transform: rotate(-90deg); }
  .side-right .word-tab { right: 0; }
  .side-right .word-tab span { transform: rotate(90deg); }
  .c-orange { background: var(--orange); }
  .c-yellow { background: var(--yellow); }
  .c-green { background: var(--green); }
  .c-teal { background: var(--teal); }
  .c-blue { background: var(--blue); }
  .c-navy { background: var(--navy); }
  .c-purple { background: var(--purple); }
  .c-magenta { background: var(--magenta); }
  .readers-art {
    position: absolute; left: 127px; top: 2067px; width: 806px; height: 340px;
    border-radius: 40px;
    background: radial-gradient(ellipse at 50% 50%, var(--art-cool), #e8ecef 75%);
  }
  .sign-off {
    position: absolute; right: 144px; top: 2428px; white-space: nowrap;
    font-family: "Special Elite", monospace; font-size: 60px; font-weight: 400; color: var(--ink);
    line-height: 1.1;
  }
</style>
</head>
<body>
<main class="bookmark">
  <svg class="frame-art" width="1200" height="2544" viewBox="0 0 1200 2544" aria-hidden="true">
    <defs>
      <linearGradient id="panelFade" x1="0" y1="0" x2="0" y2="1">
        <stop offset="0" stop-color="var(--panel-top)"/>
        <stop offset="1" stop-color="var(--panel-bottom)"/>
      </linearGradient>
    </defs>
    <path class="swoosh-red" d="M0,360 C300,220 700,140 1200,160 L1200,240 C800,215 400,280 0,430 Z" fill="var(--red)"/>
    <path class="swoosh-white" d="M0,430 C400,280 800,225 1200,240 L1200,262 C800,250 420,300 0,450 Z" fill="var(--white)"/>
    <path class="swoosh-black" d="M120,440 C480,280 880,245 1200,262 L1200,340 C900,305 520,320 120,460 Z" fill="var(--black)"/>
    <path class="writing-panel" d="M95,440 C400,295 800,290 1107,365 L1107,2512 L95,2512 Z" fill="url(#panelFade)"/>
    <rect class="base-strip" x="0" y="2512" width="1200" height="32" fill="var(--black)"/>
    <rect x="0" y="420" width="95" height="2092" fill="var(--black)"/>
    <rect x="1107" y="400" width="93" height="2112" fill="var(--black)"/>
  </svg>

  <div class="school-badge">Marrowby Lane School</div>
  <h1 class="school-name">MARROWBY LANE SCHOOL</h1>

  <div class="reader-art" role="img" aria-label="Illustration of a child lying down reading an open book"></div>
  <p class="prompt">What did you<br>think of this book?</p>

  <div class="side-left">
    <div class="word-tab c-orange" style="top:435px"><span>Interesting</span></div>
    <div class="word-tab c-yellow" style="top:694px"><span>Enthralling</span></div>
    <div class="word-tab c-green" style="top:953px"><span>Boring</span></div>
    <div class="word-tab c-teal" style="top:1212px"><span>Fantastic</span></div>
    <div class="word-tab c-blue" style="top:1471px"><span>Mysterious</span></div>
    <div class="word-tab c-navy" style="top:1730px"><span>Exciting</span></div>
    <div class="word-tab c-purple" style="top:1989px"><span>Sad</span></div>
    <div class="word-tab c-magenta" style="top:2248px"><span>Funny</span></div>
  </div>

  <div class="side-right">
    <div class="word-tab c-orange" style="top:435px"><span>Funny</span></div>
    <div class="word-tab c-yellow" style="top:694px"><span>Sad</span></div>
    <div class="word-tab c-green" style="top:953px"><span>Exciting</span></div>
    <div class="word-tab c-teal" style="top:1212px"><span>Mysterious</span></div>
    <div class="word-tab c-blue" style="top:1471px"><span>Fantastic</span></div>
    <div class="word-tab c-navy" style="top:1730px"><span>Boring</span></div>
    <div class="word-tab c-purple" style="top:1989px"><span>Enthralling</span></div>
    <div class="word-tab c-magenta" style="top:2248px"><span>Interesting</span></div>
  </div>

  <div class="readers-art" role="img" aria-label="Illustration of two children reading books around a globe with stars"></div>
  <p class="sign-off">Pass it on!</p>
</main>
</body>
</html>
```